Label and logo design for an all natural organic skincare product

We need a label design for a new company in the natural beauty space. The company is called "Kesta Tolk". "Kesta" refers to the olive tree. "Tolk" symbolizes the wren bird. The company name represents purity, nature, and freedom.

Our first product is tamanu oil - a 100% pure, organic, unrefined, cold pressed oil that is be used to improve various skin conditions (acne, eczema, scars, anti-aging) hair, and nails. Tamanu oil is a wonderful skin care healing agent that fades scars, rejuvenates skin cells, and is a powerful natural anti-aging product.

We currently do not have a company logo. We would like the logo and label to be designed together for a coordinated, well thought out, look.

We are looking for a label and logo that convey a high end quality product. We use premium quality all natural ingredients only.

Label size is 10.2cm (wide) x 4.5cm (height). The label wraps around a small amber colored glass bottle with a dropper similar to the images attached. The bottle holds 1oz (30ml) of oil.

Label will contain:
- Company logo
- Product name - "100% Pure Organic Tamanu Oil"
- Quantity - "1 fl oz / 30 ml"
- Ingredients - "100% pure virgin organic cold pressed tamanu oil (calophyllum inophyllum)
- Product Usage - "Dab a few drops of Kesta Tolk tamanu oil into your hands and rub the oil into your skin or hair 1 - 3 times a day."
- UPC barcode - will provide later
- Company info:
"Kesta Tolk
Halvern, GA
www.kestatolk.com"
- Warning - "For external use only. Do not use if you have allergies to nuts of any kind. Keep out of reach of children."

We've attached a couple images of labels that we like. In general, we prefer a modern, minimalistic, pure look but we are open to your ideas and creativity.

Colors we like: blue-green (think torquoise or tiffany blue), green, grey, white.

If you have any questions, about the design please let me know. The winning designer will be required to do a few additional tweaks to finalize the product. Thank you for your time and happy designing!

```html
<!DOCTYPE html>
<html lang="en">
<head>
<meta charset="utf-8">
<title>Kesta Tolk Tamanu Oil Label</title>
<link href="https://fonts.googleapis.com/css2?family=Jost:wght@400;500&family=Oswald:wght@400&display=swap" rel="stylesheet">
<style>
  :root {
    --teal: #1ebcb5;
    --teal-text: #17a19b;
    --ink: #1d2f30;
    --mark: #333333;
    --grey: #555555;
    --caption-orange: #c8700e;
    --caption-grey: #444444;
    --paper: #ffffff;
  }
  html, body { margin: 0; padding: 0; overflow: hidden; }
  body { width: 1200px; height: 1000px; background: var(--paper); position: relative; font-family: "Jost", sans-serif; }

  .label {
    position: absolute; left: 70px; top: 57px; width: 1077px; height: 505px;
    background: var(--paper); border: 1px solid #e4e4e4;
    box-shadow: 0 3px 10px rgba(0,0,0,0.35);
  }
  .info { position: absolute; left: 56px; font-family: "Oswald", sans-serif; font-size: 13px; line-height: 13.5px; transform: scaleX(0.82); transform-origin: left top; width: 305px; }
  .info h3 { margin: 0; font-weight: 400; font-size: 13.5px; color: var(--ink); }
  .info p { margin: 0; color: var(--teal-text); }
  .info.ingredients { top: 48px; }
  .info.usage { top: 105px; }
  .info.warning { top: 175px; }

  .brand-mark { position: absolute; left: 476px; top: 38px; width: 165px; text-align: center; }
  .brand-mark .dot { width: 114px; height: 114px; border-radius: 50%; background: var(--mark); margin: 0 auto 12px; }
  .brand-name { font-family: "Jost", sans-serif; font-weight: 400; font-size: 17px; letter-spacing: 1px; color: var(--ink); text-transform: uppercase; }

  .band { position: absolute; left: 30px; top: 239px; width: 1046px; height: 90px; background: var(--teal); }
  .band-brand { position: absolute; left: 28px; top: 10px; width: 64px; text-align: center; }
  .band-brand .dot { width: 48px; height: 48px; border-radius: 50%; background: var(--paper); margin: 0 auto 6px; }
  .band-brand .brand-name { font-size: 9px; color: var(--paper); letter-spacing: 0.5px; }
  .band-title { position: absolute; left: 100px; top: 20px; width: 142px; text-align: center; color: var(--paper); line-height: 1; }
  .band-title .pure { font-size: 11px; }
  .band-title .organic { font-size: 17px; color: var(--ink); margin: 1px 0; }
  .band-title .product { font-size: 18px; }

  .title-tab { position: absolute; left: 330px; top: 225px; width: 415px; height: 119px; background: var(--teal); border-radius: 14px; }
  .title-tab svg { position: absolute; inset: 0; }
  .title-tab .text { position: absolute; left: 0; right: 0; top: 14px; text-align: center; color: var(--paper); line-height: 1; }
  .title-tab .pure { font-size: 17px; }
  .title-tab .organic { font-size: 29px; color: var(--ink); margin: 3px 0 4px; }
  .title-tab .product { font-size: 33px; letter-spacing: 0.5px; }

  .company { position: absolute; left: 55px; top: 346px; font-family: "Oswald", sans-serif; font-size: 17px; line-height: 23px; color: var(--ink); transform: scaleX(0.85); transform-origin: left top; }
  .company p { margin: 0; }
  .eco-icons { position: absolute; left: 55px; top: 420px; display: flex; gap: 18px; }

  .net { position: absolute; left: 422px; top: 440px; font-size: 21px; color: var(--grey); }

  .caption { position: absolute; left: 107px; top: 756px; line-height: 1; }
  .caption .brand { font-family: "Oswald", sans-serif; font-size: 40px; color: var(--caption-orange); transform: scaleX(0.9); transform-origin: left top; }
  .caption .product { font-family: "Jost", sans-serif; font-size: 46px; color: var(--caption-grey); margin-top: 8px; letter-spacing: 1px; }
</style>
</head>
<body>
  <section class="label" aria-label="Tamanu oil wrap label">
    <div class="info ingredients"><h3>Ingredients</h3><p>premium quality all natural 100% pure virgin organic cold pressed tamanu oil (calophyllum inophyllum)</p></div>
    <div class="info usage"><h3>Product Usage</h3><p>Dab a few drops of Kesta Tolk tamanu oil into your hands and rub the oil into your skin or hair 1 - 3 times a day.</p></div>
    <div class="info warning"><h3>Warning</h3><p>For external use only. Do not use if you have allergies to nuts of any kind. Keep out of reach of children.</p></div>

    <div class="brand-mark">
      <div class="dot"></div>
      <div class="brand-name">Kesta Tolk</div>
    </div>

    <div class="band">
      <div class="band-brand">
        <div class="dot"></div>
        <div class="brand-name">Kesta Tolk</div>
      </div>
      <div class="band-title">
        <div class="pure">100% Pure</div>
        <div class="organic">Organic</div>
        <div class="product">TAMANU OIL</div>
      </div>
    </div>

    <div class="title-tab">
      <svg width="415" height="119" viewBox="0 0 415 119" aria-hidden="true">
        <rect x="15" y="8" width="385" height="103" rx="10" fill="none" stroke="#ffffff" stroke-width="2"/>
      </svg>
      <div class="text">
        <div class="pure">100% Pure</div>
        <div class="organic">Organic</div>
        <div class="product">TAMANU OIL</div>
      </div>
    </div>

    <div class="company">
      <p>Kesta Tolk</p>
      <p>Halvern, GA</p>
      <p>www.kestatolk.com</p>
    </div>

    <div class="eco-icons">
      <svg width="46" height="40" viewBox="0 0 46 40" role="img" aria-label="Recyclable">
        <g fill="#1d2f30">
          <path d="M17 3 L29 3 L34 12 L38 10 L34 21 L23 18 L27 16 L23 9 L18 17 L11 13 Z"/>
          <path d="M40 20 L45 30 L40 38 L30 38 L30 43 L22 34 L30 27 L30 32 L37 32 L34 26 L41 22 Z" transform="translate(0,-4)"/>
          <path d="M6 20 L13 24 L9 31 L18 31 L18 27 L25 35 L18 42 L18 37 L6 37 L1 28 Z" transform="translate(0,-4)"/>
        </g>
      </svg>
      <svg width="34" height="46" viewBox="0 0 34 46" role="img" aria-label="Dispose in bin">
        <g fill="#1d2f30">
          <circle cx="25" cy="5" r="4"/>
          <path d="M21 11 h8 v16 h-2 v17 h-4 v-17 h-2 z"/>
          <path d="M20 14 L12 20 L13 22 L21 17 Z"/>
          <path d="M2 22 h12 l-1.5 22 h-9 z" fill="none" stroke="#1d2f30" stroke-width="2"/>
          <rect x="1" y="19" width="14" height="2"/>
        </g>
      </svg>
    </div>

    <div class="net">Net 1 fl oz / 30ml &#8494;</div>
  </section>

  <div class="caption">
    <div class="brand">Kesta Tolk</div>
    <div class="product">TAMANU OIL</div>
  </div>
</body>
</html>
```